Brightwell Pictures Business Card

Hello,

i would like to have a dynamic, creative but tasteful card, colour used, front and back. I have attached a sample card that I liked very much from another individual to give you an idea of the theme/approach, but not colour. Ideally the graphic elements of the Brightwell Logo are brought into the design.

Target Market(s)

North America

Industry/Entity Type

Film Production

Contact Information for Business Card

Mirela Vantasch
President/Founder
Brightwell Pictures Inc.
587 914 3362
mirela@brightwellpix.tv

Font styles to use
Sans Serif

Colors
6b449b
5c5c5c
fdfdfd
000000

Requirements
Must have
• Logo, name, Company name, email and cell number. no Address line to be included.
Should not have
• any unrelated GFX elements, serif fonts

```html
<!DOCTYPE html>
<html lang="en">
<head>
<meta charset="utf-8">
<title>Brightwell Pictures Business Card</title>
<link href="https://fonts.googleapis.com/css2?family=Lato:wght@400;700;900&display=swap" rel="stylesheet">
<style>
  :root {
    --page: #1c1c1e;
    --card: #5c5c5c;
    --accent: #6b449b;
    --ink: #fdfdfd;
    --ink-soft: #e6e6e6;
  }
  * { margin: 0; padding: 0; box-sizing: border-box; }
  html, body {
    width: 1200px; height: 1200px; overflow: hidden;
    background: var(--page);
    font-family: "Lato", Arial, sans-serif;
    color: var(--ink);
  }
  .stage {
    position: relative; width: 1200px; height: 1200px;
    display: flex; flex-direction: column; align-items: center; justify-content: center;
    gap: 44px;
  }
  .card {
    position: relative; width: 860px; height: 491px;
    background: var(--card);
    box-shadow: 0 18px 40px rgba(0,0,0,0.45);
    overflow: hidden;
  }
  .card-edge {
    position: absolute; left: 0; bottom: 0; width: 100%; height: 10px; background: var(--accent);
  }
  /* Front */
  .card-front { display: flex; align-items: center; justify-content: center; }
  .brand-front { display: flex; align-items: center; gap: 18px; }
  .brand-dot {
    width: 28px; height: 28px; border-radius: 50%; background: var(--accent); flex: none;
  }
  .brand-name-front {
    font-weight: 900; font-size: 62px; letter-spacing: -1px; line-height: 1; color: var(--ink);
  }
  /* Back */
  .brand-side {
    position: absolute; left: 80px; top: 245px;
    transform: translate(-50%, -50%) rotate(-90deg);
    white-space: nowrap;
    font-weight: 900; font-size: 40px; letter-spacing: -0.5px; line-height: 1; color: var(--ink);
  }
  .divider-vertical {
    position: absolute; left: 150px; top: 60px; width: 3px; height: 370px; background: var(--accent);
  }
  .contact-block { position: absolute; left: 215px; top: 105px; }
  .person-name { font-size: 42px; font-weight: 400; line-height: 1.05; }
  .person-title { font-size: 24px; font-weight: 400; color: var(--ink-soft); margin-top: 2px; }
  .company-name { font-size: 18px; font-weight: 400; color: var(--ink-soft); margin-top: 14px; }
  .divider-horizontal { width: 340px; height: 3px; background: var(--accent); margin: 32px 0 28px; }
  .contact-row { display: flex; align-items: center; gap: 14px; font-size: 26px; margin-bottom: 10px; }
  .contact-row svg { width: 26px; height: 26px; flex: none; }
  .contact-sep { margin-right: 4px; }
</style>
</head>
<body>
<main class="stage">
  <section class="card card-front" aria-label="Card front">
    <div class="brand-front">
      <span class="brand-dot"></span>
      <span class="brand-name-front">Brightwell Pictures</span>
    </div>
    <div class="card-edge"></div>
  </section>

  <section class="card card-back" aria-label="Card back">
    <div class="brand-side">Brightwell Pictures</div>
    <div class="divider-vertical"></div>
    <div class="contact-block">
      <h1 class="person-name">Mirela Vantasch</h1>
      <p class="person-title">President/Founder</p>
      <p class="company-name">Brightwell Pictures Inc.</p>
      <div class="divider-horizontal"></div>
      <p class="contact-row">
        <svg viewBox="0 0 26 26" aria-hidden="true">
          <circle cx="13" cy="13" r="11.5" fill="none" stroke="#fdfdfd" stroke-width="1.6"/>
          <path d="M9.5 7.5 l2 0 l1 3 l-1.5 1.2 a7 7 0 0 0 3.3 3.3 l1.2 -1.5 l3 1 l0 2 a1.5 1.5 0 0 1 -1.6 1.5 a10 10 0 0 1 -9 -9 a1.5 1.5 0 0 1 1.6 -1.5z" fill="none" stroke="#fdfdfd" stroke-width="1.4" stroke-linejoin="round"/>
        </svg>
        <span class="contact-sep">:</span>587 914 3362
      </p>
      <p class="contact-row">
        <svg viewBox="0 0 26 26" aria-hidden="true">
          <rect x="2" y="6" width="22" height="14" fill="none" stroke="#fdfdfd" stroke-width="1.6"/>
          <path d="M2 6 L13 15 L24 6" fill="none" stroke="#fdfdfd" stroke-width="1.6"/>
        </svg>
        <span class="contact-sep">:</span>mirela@brightwellpix.tv
      </p>
    </div>
    <div class="card-edge"></div>
  </section>
</main>
</body>
</html>
```